Aesthetics Company Flyer (description of services)

We need a 5.5"x8.5" flyer describing the services we offer at velvet horizon aesthetics. We are an aesthetics company located in Conroe TX. Our products and services can be found at www.vhaesthetics-demo.com/services . We would like to see designs that are cohesive with our brand and website: https://www.vhaesthetics-demo.com/

```html
<!DOCTYPE html>
<html lang="en">
<head>
<meta charset="utf-8">
<title>Velvet Horizon Aesthetics – Services Flyer</title>
<link href="https://fonts.googleapis.com/css2?family=Montserrat:wght@400;600;700;800&family=Open+Sans:wght@400;600&display=swap" rel="stylesheet">
<style>
:root{
  --lavender:#a98fc6;
  --lavender-soft:#e3d9ee;
  --pink:#d88fbf;
  --ink:#161616;
  --grey:#5a5a5a;
  --paper:#ffffff;
  --stage:#e9e7ec;
}
*{box-sizing:border-box;margin:0;padding:0}
html,body{width:889px;height:1200px;overflow:hidden;background:var(--stage)}
body{position:relative;font-family:'Open Sans',Arial,sans-serif;color:var(--ink)}
.page{position:absolute;top:279px;width:415px;height:642px;background:var(--paper);box-shadow:0 4px 14px rgba(0,0,0,.18);overflow:hidden}
.page--front{left:20px}
.page--back{left:454px}
.abs{position:absolute}
.brand{display:flex;align-items:center;gap:6px;font-family:'Montserrat',sans-serif;font-weight:600;font-size:9px;color:var(--lavender);text-transform:lowercase;line-height:1.1}
.brand__dot{width:22px;height:22px;border-radius:50%;background:var(--lavender-soft);flex:none}
.headline{font-family:'Montserrat',sans-serif;font-weight:700;text-transform:uppercase;color:var(--lavender);font-size:17px;line-height:1.2;letter-spacing:.3px}
.headline em{font-style:normal;color:var(--pink)}
.accent-band{background:var(--lavender-soft)}
.photo{background:linear-gradient(135deg,#e6d2bf,#b98f70 55%,#4a3629)}
.promo{background:var(--ink);color:#fff;font-family:'Montserrat',sans-serif;font-weight:800;text-transform:uppercase;font-size:17px;line-height:1.15;padding:16px 14px}
.promo em{font-style:normal;color:var(--lavender)}
.promo__img{position:absolute;left:14px;right:14px;bottom:12px;height:58px;background:linear-gradient(135deg,#e9c7c0,#a7826f)}
.body-copy{font-size:7.5px;line-height:1.45;color:var(--grey)}
.body-copy strong{color:var(--lavender)}
.phone{display:flex;align-items:center;gap:6px;font-family:'Montserrat',sans-serif;font-weight:800;font-size:24px;color:var(--ink);white-space:nowrap}
.contact{font-size:7px;line-height:1.6;color:var(--grey)}
.contact b{color:var(--ink)}
.footer-bar{left:0;right:0;bottom:0;height:14px;background:var(--ink)}
.footer-bar::before{content:"";position:absolute;left:0;top:0;width:120px;height:14px;background:var(--lavender)}
.section-title{left:0;right:0;text-align:center;font-family:'Montserrat',sans-serif;font-weight:800;font-size:18px;letter-spacing:.5px}
.section-title::after{content:"";display:block;width:40px;height:3px;background:var(--lavender);margin:5px auto 0}
.services{left:26px;right:26px;top:70px;display:grid;grid-template-columns:repeat(3,1fr);gap:14px 16px}
.service__img{height:66px}
.service__name{margin-top:5px;text-align:center;font-family:'Montserrat',sans-serif;font-weight:600;font-size:8.5px}
.service__name small{display:block;font-weight:400;font-size:6.5px;color:var(--grey)}
.tone-1{background:linear-gradient(135deg,#f1e2d8,#c9a892)}
.tone-2{background:linear-gradient(135deg,#e7d3cf,#a98a86)}
.tone-3{background:linear-gradient(135deg,#f0d9d5,#c7a2a0)}
.tone-4{background:linear-gradient(135deg,#d9c9e6,#8e78a8)}
.tone-5{background:linear-gradient(135deg,#f3e3c9,#cba37b)}
.tone-6{background:linear-gradient(135deg,#e6eef0,#9fb7bf)}
.iv{left:26px;right:26px;top:342px;display:grid;grid-template-columns:repeat(3,1fr);gap:9px 14px}
.iv__name{font-family:'Montserrat',sans-serif;font-weight:700;font-size:7.5px;color:var(--lavender)}
.iv__text{font-size:6.3px;line-height:1.35;color:var(--grey)}
.back-foot{left:26px;right:26px;bottom:28px;display:flex;align-items:center;justify-content:space-between}
.book{font-size:7px;color:var(--grey);text-align:center}
.book .phone{font-size:16px}
</style>
</head>
<body>

<section class="page page--front">
  <div class="abs brand" style="left:18px;top:20px;width:110px">
    <span class="brand__dot"></span><span>velvet horizon aesthetics</span>
  </div>
  <h1 class="abs headline" style="left:140px;top:18px;width:260px">Everyone is beautiful. With us, everyone can feel <em>beautiful too</em></h1>
  <div class="abs accent-band" style="left:140px;top:86px;width:120px;height:6px"></div>

  <div class="abs photo" role="img" aria-label="Portrait photo of two smiling women with glowing skin" style="left:0;top:108px;width:300px;height:270px"></div>
  <div class="abs promo" style="left:236px;top:132px;width:164px;height:220px">
    We change <em>the world</em> one beautiful face <em>at a time</em>
    <div class="promo__img" role="img" aria-label="Close-up photo of a facial skincare treatment"></div>
  </div>
  <div class="abs" style="left:300px;top:358px;width:115px;height:20px;background:var(--lavender)"></div>

  <p class="abs body-copy" style="left:18px;top:396px;width:180px"><strong>Velvet Horizon Aesthetics</strong> – we offer a comprehensive list of services, Injectables, Skincare and Weightloss Services and IV Hydration Therapy.</p>
  <p class="abs body-copy" style="left:214px;top:396px;width:184px">We take pride in our care, tailoring every treatment to help you look and feel your best.</p>

  <div class="abs phone" style="left:18px;top:468px">
    <svg width="22" height="22" viewBox="0 0 24 24" aria-hidden="true"><circle cx="12" cy="12" r="12" fill="var(--lavender)"/><path d="M8.5 6.5l2 2.2-1.2 1.5c.8 1.7 2 2.9 3.6 3.7l1.5-1.2 2.2 2-1.1 2.1c-4.6-.4-8.3-4.1-8.7-8.7z" fill="#fff"/></svg>
    555 014 2290
  </div>
  <div class="abs contact" style="left:230px;top:462px;width:170px">
    <b>555 014 2290</b><br>2110 Sample Road, Conroe TX<br>www.vhaesthetics-demo.com/services
  </div>
  <div class="abs accent-band" style="left:18px;top:540px;width:380px;height:6px"></div>
  <div class="abs footer-bar"></div>
</section>

<section class="page page--back">
  <h2 class="abs section-title" style="top:26px">OUR SERVICES</h2>
  <div class="abs services">
    <div><div class="service__img tone-1" role="img" aria-label="Photo of a measuring tape around a waist"></div><p class="service__name">Weightloss</p></div>
    <div><div class="service__img tone-2" role="img" aria-label="Photo of a forehead injection treatment"></div><p class="service__name">Neurotoxin<small>(Wrinkle Relaxer)</small></p></div>
    <div><div class="service__img tone-3" role="img" aria-label="Photo of a lip filler treatment"></div><p class="service__name">Dermal Fillers</p></div>
    <div><div class="service__img tone-4" role="img" aria-label="Photo of a growth factor facial"></div><p class="service__name">Fibrin Growth Factor<small>(PRF)</small></p></div>
    <div><div class="service__img tone-5" role="img" aria-label="Photo of a microneedling treatment"></div><p class="service__name">MicroNeedle Pen</p></div>
    <div><div class="service__img tone-6" role="img" aria-label="Photo of a chemical peel application"></div><p class="service__name">Chemical Peels</p></div>
  </div>

  <h2 class="abs section-title" style="top:300px">IV HYDRATION</h2>
  <div class="abs iv">
    <div><p class="iv__name">Quench Hydrate</p><p class="iv__text">Fluids and electrolytes restore.</p></div>
    <div><p class="iv__name">Glutathione</p><p class="iv__text">Antioxidant for brighter skin.</p></div>
    <div><p class="iv__name">Myers Cocktail</p><p class="iv__text">Vitamins for daily wellness.</p></div>
    <div><p class="iv__name">Hangover Relief</p><p class="iv__text">Rehydrate and ease headaches.</p></div>
    <div><p class="iv__name">Immune Boost</p><p class="iv__text">Vitamin C supports defenses.</p></div>
    <div><p class="iv__name">NAD+ Boost</p><p class="iv__text">Cellular energy and focus.</p></div>
    <div><p class="iv__name">Energy Tonic</p><p class="iv__text">B vitamins fight fatigue.</p></div>
    <div><p class="iv__name">Athletic Recovery</p><p class="iv__text">Amino acids repair muscles.</p></div>
    <div><p class="iv__name">Migraine Rescue</p><p class="iv__text">Fast relief from pain.</p></div>
    <div><p class="iv__name">Beauty Glow</p><p class="iv__text">Biotin for hair, nails.</p></div>
    <div><p class="iv__name">Detox Drip</p><p class="iv__text">Flush toxins, feel renewed.</p></div>
    <div><p class="iv__name">Post Workout Recovery</p><p class="iv__text">Replenish after hard training.</p></div>
  </div>

  <div class="abs back-foot">
    <div class="brand" style="width:100px"><span class="brand__dot"></span><span>velvet horizon aesthetics</span></div>
    <div class="book">Please Call to Book
      <div class="phone">
        <svg width="16" height="16" viewBox="0 0 24 24" aria-hidden="true"><circle cx="12" cy="12" r="12" fill="var(--lavender)"/><path d="M8.5 6.5l2 2.2-1.2 1.5c.8 1.7 2 2.9 3.6 3.7l1.5-1.2 2.2 2-1.1 2.1c-4.6-.4-8.3-4.1-8.7-8.7z" fill="#fff"/></svg>
        555 014 2290
      </div>
    </div>
    <div class="contact"><b>555 014 2290</b><br>2110 Sample Road<br>Conroe TX</div>
  </div>
  <div class="abs footer-bar"></div>
</section>

</body>
</html>
```